Vesk Architecture

We are a architectural design and build company working between scales 1/1000 to 1/1 we want people to understand our difference from our design experience and quality.we build hotels restourants and office spaces.Our company name is Vesk architecture to mind sustainability.

We want to write our adress phone and work spesifications on the card and we want our logo as backround.

Ps:you could find the logo adress and phone box numbers from the web:www.veskmimarlik-ornek.com

Target Market(s)

Who looks for experts.

Industry/Entity Type

Architecture

Requirements
Must have
• Design is over everything.
Should not have
• we don want it to be colorfull

```html
<!DOCTYPE html>
<html lang="tr">
<head>
<meta charset="utf-8">
<title>Vesk Architecture – Business Card</title>
<link rel="stylesheet" href="https://fonts.googleapis.com/css2?family=Open+Sans:wght@400;600&display=swap">
<style>
  :root {
    --sheet: #ffffff;
    --frame-edge: #c9c9c9;
    --card-dark: #3a3a3a;
    --card-light: #ffffff;
    --ink: #2e2e2e;
    --crop: #555555;
    --shadow: rgba(0,0,0,0.35);
  }
  * { box-sizing: border-box; margin: 0; padding: 0; }
  html, body { width: 1200px; height: 447px; overflow: hidden; background: var(--sheet); }
  .presentation {
    position: relative;
    width: 1200px; height: 447px;
    background: var(--sheet);
    box-shadow: inset 0 0 22px 10px var(--frame-edge);
    font-family: "Open Sans", Verdana, sans-serif;
  }
  .card {
    position: absolute;
    top: 97px;
    width: 437px; height: 250px;
    box-shadow: 6px 8px 10px var(--shadow);
    background: var(--card-light);
  }
  .card--front { left: 97px; }
  .card--back  { left: 658px; }
  .crop-marks { position: absolute; left: -20px; top: -20px; width: 477px; height: 290px; overflow: visible; }
  .crop-marks line { stroke: var(--crop); stroke-width: 1; }

  .front-mark {
    position: absolute;
    left: 14px; top: 0; bottom: 0;
    width: 92px;
    display: flex; flex-direction: column; align-items: center; justify-content: center; gap: 12px;
    color: var(--card-dark);
    font-weight: 600;
    font-size: 27px;
    letter-spacing: 2px;
  }
  .front-mark__dot { width: 46px; height: 46px; border-radius: 50%; background: var(--card-dark); }

  .contact {
    position: absolute;
    left: 105px; top: 92px;
    width: 300px;
    text-align: center;
    color: var(--ink);
    font-style: normal;
    font-size: 13.5px;
    line-height: 17px;
    letter-spacing: 0.6px;
  }

  .brand-panel {
    position: absolute; left: 0; top: 0;
    width: 100%; height: 216px;
    background: var(--card-dark);
  }
  .brand-name {
    position: absolute; left: 0; right: 0; top: 82px;
    display: flex; align-items: center; justify-content: center; gap: 14px;
    color: var(--card-light);
    font-weight: 600;
    font-size: 34px;
    letter-spacing: 3px;
  }
  .brand-dot { width: 18px; height: 18px; border-radius: 50%; background: var(--card-light); }
  .website {
    position: absolute; left: 0; right: 0; top: 223px;
    text-align: center;
    color: var(--ink);
    font-weight: 600;
    font-size: 15px;
    letter-spacing: 1px;
  }
</style>
</head>
<body>
<main class="presentation">
  <section class="card card--front" aria-label="Card front">
    <svg class="crop-marks" viewBox="0 0 477 290" aria-hidden="true">
      <line x1="20" y1="0" x2="20" y2="12"/><line x1="0" y1="20" x2="12" y2="20"/>
      <line x1="457" y1="0" x2="457" y2="12"/><line x1="465" y1="20" x2="477" y2="20"/>
      <line x1="20" y1="278" x2="20" y2="290"/><line x1="0" y1="270" x2="12" y2="270"/>
      <line x1="457" y1="278" x2="457" y2="290"/><line x1="465" y1="270" x2="477" y2="270"/>
    </svg>
    <div class="front-mark">
      <span class="front-mark__dot" aria-hidden="true"></span>
      <span>VESK</span>
    </div>
    <address class="contact">
      Ihlamur Mah. Serin Cad. Yaprak Sok.<br>
      No:7 Kuzey Kadikoy/Istanbul<br>
      T.0216 555 01 47 F. 0216 555 01 48<br>
      E-mail:studio@veskmimarlik-ornek.com
    </address>
  </section>

  <section class="card card--back" aria-label="Card back">
    <svg class="crop-marks" viewBox="0 0 477 290" aria-hidden="true">
      <line x1="20" y1="0" x2="20" y2="12"/><line x1="0" y1="20" x2="12" y2="20"/>
      <line x1="457" y1="0" x2="457" y2="12"/><line x1="465" y1="20" x2="477" y2="20"/>
      <line x1="20" y1="278" x2="20" y2="290"/><line x1="0" y1="270" x2="12" y2="270"/>
      <line x1="457" y1="278" x2="457" y2="290"/><line x1="465" y1="270" x2="477" y2="270"/>
    </svg>
    <div class="brand-panel">
      <p class="brand-name"><span class="brand-dot" aria-hidden="true"></span>VESK MİMARLIK</p>
    </div>
    <p class="website">www.veskmimarlik-ornek.com</p>
  </section>
</main>
</body>
</html>
```